Portraits by Hilda

My product is custom pet portraits. I have never had a card made up. All new to me. I would like double sided. One side with my Title and contact info with a small painting I have developed. And the other side have another painting of mine almost the full size of card. With a pretty border of Valmoret design. I would also like the Valmoret design incorporated in the front somehow maybe as a border I haven't really thought of a title for my business. Any suggestions.? Color choices I would like would be pinks, greens yellows blue tones. You will see in my paintings my style. I have enclosed two photos not sure which would look better on front or back. You could also incorporate some type of flower or scroll/like flower

Target Market(s)

Pet lovers

Industry/Entity Type

Pet

Contact Information for Business Card

Hilda Ostrander(612)-867-6630

Font styles to use
Decorative
Script

Colors
3277b5
ec1f27
e667a6
fece3e
add136
2fb7a3

Requirements
Must have
• My name, phone number and email on the front. A photo on the backside and scroll font on the front. With a pretty Valmoret type border maybe. Would like to see my last photo - I have sent updated photos. I would like the cat and a dog on the card with pretty type border. Would also like the corners of card to be rounded or curved and thinker type paper. I think the cavalier dog would be cute with the cat. see what you can come up with.
Nice to have
• I would like to change this again. I want to gear this to all animals. I would like my cat and a dog on the card. Front and back.
Should not have
• No telephone beside my phone number. No printed font. No contemporary style. I prefer a traditional and more vintage look. I have deleted the flower painting. Let's stink with just the animals I have loaded I have deleted the two dogs. Not crazy about having them in

```html
<!DOCTYPE html>
<html lang="en">
<head>
<meta charset="utf-8">
<title>Portraits by Hilda – Business Card</title>
<link rel="stylesheet" href="https://fonts.googleapis.com/css2?family=Great+Vibes&family=Cormorant+Garamond:wght@500&family=Arimo:wght@400&display=swap">
<style>
  :root {
    --stage: #2b2b2b;
    --card-cream: #ece6d1;
    --pattern-light: #efe9d4;
    --pattern-tan: #d9ccaa;
    --gold-light: #f7d65a;
    --gold-mid: #e2a91c;
    --gold-dark: #a8740c;
    --silver-light: #b3a9bd;
    --silver-mid: #7f7489;
    --silver-dark: #4d4456;
    --canvas-blue: #3277b5;
    --canvas-blue-deep: #1f3f8a;
    --canvas-navy: #16245e;
    --fur-cream: #efe6cf;
    --fur-lilac: #c9c3dc;
    --fur-gold: #d9a24a;
    --name-brown: #7a3a1c;
    --ink: #1c1a18;
  }
  * { box-sizing: border-box; margin: 0; padding: 0; }
  html, body { width: 1200px; height: 900px; overflow: hidden; }
  body { background: var(--stage); position: relative; }

  .card {
    position: absolute;
    left: 250px;
    width: 700px;
    height: 400px;
    box-shadow: 0 8px 24px rgba(0,0,0,0.5);
  }

  /* Back: full painting inside a gold frame */
  .card-back { top: 35px; }
  .gold-frame {
    width: 100%;
    height: 100%;
    padding: 28px;
    position: relative;
    background: linear-gradient(135deg, var(--gold-light), var(--gold-mid) 40%, var(--gold-dark) 62%, var(--gold-light) 85%, var(--gold-mid));
  }
  .gold-frame::before,
  .gold-frame::after {
    content: "";
    position: absolute;
    pointer-events: none;
  }
  .gold-frame::before { inset: 8px; border: 2px solid rgba(255, 240, 170, 0.7); }
  .gold-frame::after { inset: 22px; border: 3px solid var(--gold-dark); }
  .painting-large {
    width: 100%;
    height: 100%;
    background:
      linear-gradient(100deg, var(--canvas-blue) 0%, var(--canvas-blue) 32%, var(--fur-lilac) 42%, var(--fur-cream) 55%, var(--fur-cream) 78%, var(--fur-lilac) 90%, var(--canvas-blue) 100%);
  }

  /* Front: patterned card with framed painting and contact */
  .card-front {
    top: 465px;
    background: var(--card-cream);
    overflow: hidden;
  }
  .fret-pattern {
    position: absolute;
    inset: 0;
    background: linear-gradient(160deg, var(--pattern-light) 0%, var(--pattern-tan) 55%, var(--pattern-light) 100%);
  }
  .silver-frame {
    position: absolute;
    left: 42px;
    top: 72px;
    width: 322px;
    height: 252px;
    padding: 20px;
    background: linear-gradient(135deg, var(--silver-light), var(--silver-mid) 50%, var(--silver-dark));
    box-shadow: 5px 7px 12px rgba(0,0,0,0.4);
  }
  .silver-frame::after {
    content: "";
    position: absolute;
    inset: 6px;
    border: 2px solid rgba(230, 222, 240, 0.45);
    pointer-events: none;
  }
  .painting-small {
    width: 100%;
    height: 100%;
    border: 2px solid var(--silver-dark);
    background: linear-gradient(180deg, var(--canvas-blue) 0%, var(--fur-gold) 35%, var(--fur-gold) 62%, var(--canvas-navy) 100%);
  }

  .contact {
    position: absolute;
    left: 390px;
    top: 128px;
    width: 290px;
    text-align: center;
  }
  .contact-name {
    font-family: "Great Vibes", cursive;
    font-size: 44px;
    font-weight: 400;
    color: var(--name-brown);
    line-height: 1.05;
    white-space: nowrap;
  }
  .contact-title {
    font-family: "Cormorant Garamond", serif;
    font-size: 22px;
    font-weight: 500;
    color: var(--ink);
    margin-top: 2px;
    line-height: 1.2;
  }
  .contact-phone {
    font-family: "Arimo", sans-serif;
    font-size: 23px;
    color: var(--ink);
    margin-top: 2px;
    line-height: 1.2;
  }
</style>
</head>
<body>
  <section class="card card-back" aria-label="Card back">
    <div class="gold-frame">
      <div class="painting-large" role="img" aria-label="Painted portrait of a fluffy white dog on a blue background"></div>
    </div>
  </section>

  <section class="card card-front" aria-label="Card front">
    <div class="fret-pattern" role="img" aria-label="Woven cream and tan fret pattern background"></div>
    <div class="silver-frame">
      <div class="painting-small" role="img" aria-label="Painted portrait of a golden retriever holding a tennis ball in blue water"></div>
    </div>
    <div class="contact">
      <h1 class="contact-name">Hilda Ostrander</h1>
      <p class="contact-title">Custom Pet Portraits</p>
      <p class="contact-phone">(555)-214-3981</p>
    </div>
  </section>
</body>
</html>
```